Business Card Design for company

We want new business cards. We'd like something different-- yet still highly professional. Our tagline is Providing leadership, delivering success. Stock photos are ok, as long as they are relevant and look upscale.

Target Market(s)

Architecture/Business Management Consulting/Engineering Consulting

Contact Information for Business Card

dark gray background with pops of blue might be good, but you tell me. You're the designers. Rounded corners might be nice, but again, you tell me.

Font styles to use
Serif
Sans Serif

Colors
3276b5
5c5c5c
9d9d9d
fbfbfb

Requirements
Nice to have
• Something different, but still very professional.

```html
<!DOCTYPE html>
<html lang="en">
<head>
<meta charset="utf-8">
<title>Norvale – Business Card</title>
<link rel="stylesheet" href="https://fonts.googleapis.com/css2?family=Josefin+Sans:wght@400;600&family=Montserrat:wght@500&display=swap">
<style>
  :root {
    --stage: #333333;
    --blue: #3276b5;
    --blue-deep: #1f4f86;
    --sky: #c9dcee;
    --grey: #9d9d9d;
    --ink: #111111;
    --paper: #ffffff;
    --mist: #fbfbfb;
  }
  html, body {
    margin: 0;
    width: 1200px;
    height: 1112px;
    overflow: hidden;
    background: var(--stage);
  }
  .card {
    position: absolute;
    width: 397px;
    height: 642px;
    transform: scale(0.8114);
    transform-origin: top left;
    overflow: hidden;
    font-family: "Josefin Sans", sans-serif;
  }
  .card--front { left: 226px; top: 315px; background: var(--paper); }
  .card--back { left: 649px; top: 312px; height: 646px; background: var(--paper); }
  .card__art { position: absolute; inset: 0; width: 100%; height: 100%; }
  .brand {
    position: absolute;
    left: 0; right: 0;
    text-align: center;
    font-family: "Montserrat", sans-serif;
    font-weight: 500;
    color: var(--blue-deep);
    letter-spacing: 2px;
    margin: 0;
  }
  .card--front .brand { top: 48px; font-size: 40px; }
  .card--back .brand { top: 272px; font-size: 40px; }
  .holder {
    position: absolute; left: 0; right: 0; top: 344px;
    text-align: center; margin: 0;
    font-weight: 600; font-size: 36px; letter-spacing: 1px;
    color: var(--ink);
  }
  .role {
    position: absolute; left: 0; right: 0; top: 382px;
    text-align: center; margin: 0;
    font-size: 13px; color: var(--ink);
  }
  .contact {
    position: absolute; left: 0; right: 0;
    text-align: center; margin: 0;
    color: var(--ink);
  }
  .contact--phone { top: 436px; font-size: 12px; }
  .contact--web { top: 465px; font-size: 13px; }
  .contact--address { top: 493px; font-size: 9.5px; line-height: 14px; }
  .email {
    position: absolute; left: 0; right: 0; top: 611px;
    text-align: center; margin: 0;
    font-size: 13px; color: var(--paper);
  }
  .card--back .email { top: 615px; }
</style>
</head>
<body>

<section class="card card--front">
  <svg class="card__art" viewBox="0 0 397 642">
    <defs>
      <linearGradient id="frontSky" x1="0" y1="0" x2="1" y2="1">
        <stop offset="0" stop-color="#2c5f96"/>
        <stop offset="0.45" stop-color="#c9dcee"/>
        <stop offset="1" stop-color="#1d3f6a"/>
      </linearGradient>
    </defs>
    <polygon role="img" aria-label="Upward view of glass office towers against the sky"
             points="0,0 397,0 397,190 199,340 0,172" fill="url(#frontSky)"/>
    <polygon class="accent" points="0,160 199,340 40,190" fill="var(--blue)"/>
    <polygon class="accent" points="397,175 199,340 360,210" fill="var(--blue)"/>
    <polygon class="veil" points="75,0 324,0 324,200 199,335 75,228" fill="#ffffff" opacity="0.72"/>
    <polygon class="base" points="0,422 199,597 397,422 397,642 0,642" fill="var(--grey)"/>
  </svg>
  <p class="brand">NORVALE</p>
  <h1 class="holder">FARID</h1>
  <p class="role">GRAND MANAGER</p>
  <p class="contact contact--phone">123 - 456 - 789</p>
  <p class="contact contact--web">YOURWEBSITE.COM</p>
  <p class="contact contact--address">LAKEVIEW ROAD, BLOCK 4<br>NORTHFIELD 20410</p>
  <p class="email">EMAIL@WEBSITE.COM</p>
</section>

<section class="card card--back">
  <svg class="card__art" viewBox="0 0 397 646">
    <defs>
      <linearGradient id="backSky" x1="0" y1="0" x2="1" y2="1">
        <stop offset="0" stop-color="#2a5585"/>
        <stop offset="0.4" stop-color="#d6e4f1"/>
        <stop offset="0.75" stop-color="#3276b5"/>
        <stop offset="1" stop-color="#173a63"/>
      </linearGradient>
    </defs>
    <rect class="base" x="0" y="0" width="397" height="646" fill="var(--grey)"/>
    <polygon role="img" aria-label="Upward view of glass office towers against the sky"
             points="0,0 397,0 397,428 198,601 0,428" fill="url(#backSky)"/>
    <polygon class="veil" points="75,0 322,0 322,420 198,588 75,420" fill="#ffffff" opacity="0.72"/>
  </svg>
  <p class="brand">NORVALE</p>
  <p class="email">EMAIL@WEBSITE.COM</p>
</section>

</body>
</html>
```